Brightwell Giving Inc

We need a full re-design of our non-profit organization website (www.brightwellgiving.org). Ideally, we are looking to make it more attractive, user-friendly, and interactive with our business model.

Please make sure to user colors that ago with our logo.

We need a homepage done and we also need a content page done where we will use for the other pages to fill with content.

Target Market(s)

Clothes/textiles donations.

Industry/Entity Type

Charity

Number of Pages Required

2 page

Colors

Designer to choose colors to be used in the design.

Requirements
Must have
• It must match the styling of our logo and same colors as current website. (www.brightwellgiving.org)
Nice to have
• Sleek homepage that is easy to understand and get our main points across.

```html
<!DOCTYPE html>
<html lang="en">
<head>
<meta charset="utf-8">
<title>Brightwell Giving Inc</title>
<link href="https://fonts.googleapis.com/css2?family=Open+Sans:ital,wght@0,400;0,600;0,700;1,700&family=Roboto+Condensed:wght@400;700&display=swap" rel="stylesheet">
<style>
:root{
  --green:#3b8f2a;
  --green-dark:#2d6f20;
  --orange:#f5a21b;
  --red:#c8272d;
  --ink:#2b2b2b;
  --muted:#6f6f6f;
  --line:#e3e3e3;
  --topbar:#f4f4f4;
  --footer:#1f1f1f;
  --white:#ffffff;
}
*{box-sizing:border-box;margin:0;padding:0}
html,body{width:1200px;height:2784px;overflow:hidden}
body{font-family:"Open Sans",Arial,sans-serif;color:var(--ink);background:var(--white);font-size:13px;line-height:1.6}
h1,h2,h3,h4{font-family:"Roboto Condensed","Arial Narrow",sans-serif;font-weight:700}
.wrap{width:1080px;margin:0 auto;position:relative}
.btn{display:inline-block;background:var(--green);color:var(--white);font-size:12px;font-weight:600;padding:7px 18px;border-radius:3px;text-decoration:none}

/* top bar */
.topbar{height:24px;background:var(--topbar);border-bottom:1px solid var(--line);font-size:11px;color:var(--muted)}
.topbar .wrap{display:flex;justify-content:space-between;align-items:center;height:24px}
.topbar span{margin-right:22px}

/* header */
.header{height:58px;background:var(--white)}
.header .wrap{display:flex;align-items:center;height:58px}
.brand{display:flex;align-items:center;gap:10px;width:260px}
.brand-mark{width:34px;height:34px;border-radius:50%;background:var(--green)}
.brand-name{font-family:"Roboto Condensed",sans-serif;font-weight:700;font-size:20px;color:var(--green);line-height:1}
.nav{display:flex;gap:26px;flex:1;font-size:12px;font-weight:600;text-transform:uppercase}
.nav a{color:var(--ink);text-decoration:none}
.nav a.active{color:var(--green)}
.social{display:flex;gap:8px}
.social i{width:26px;height:26px;border-radius:50%;display:block}
.social i:nth-child(1){background:#3b5998}
.social i:nth-child(2){background:#29a9e1}
.social i:nth-child(3){background:var(--red)}

/* hero */
.hero{height:390px;position:relative;background:linear-gradient(90deg,#7a6a58 0%,#9c8a74 35%,#6d6a5e 70%,#4e5149 100%)}
.hero-photo{position:absolute;inset:0}
.hero-copy{position:absolute;left:640px;top:120px;width:440px;color:var(--white)}
.hero-copy h1{font-size:38px;line-height:1.15;font-style:italic;text-transform:uppercase}
.hero-copy h1 em{color:var(--orange);font-style:italic}
.hero-copy p{font-size:14px;margin:14px 0 22px;font-style:italic}

/* about */
.about{padding:100px 0 0;height:520px}
.about .wrap{display:flex;gap:60px}
.about-text{width:500px}
.about-text h2{font-size:26px;text-transform:uppercase;margin-bottom:14px;border-bottom:2px solid var(--line);padding-bottom:8px}
.about-text p{color:var(--muted);margin-bottom:12px}
.ticks{list-style:none;width:520px;padding-top:4px}
.ticks li{display:flex;align-items:center;gap:12px;font-size:11px;text-transform:uppercase;color:var(--muted);padding:10px 0}
.ticks svg{flex:none}

/* work */
.work{height:300px}
.section-title{text-align:center;font-size:30px;margin-bottom:24px}
.work-grid{display:grid;grid-template-columns:repeat(4,1fr);gap:14px}
.work-tile{height:196px;position:relative;border-radius:2px}
.work-tile span{position:absolute;left:0;right:0;bottom:0;background:rgba(0,0,0,.55);color:var(--white);font-size:13px;padding:6px 10px}
.work-tile:nth-child(1){background:linear-gradient(#8f7a63,#5f5448)}
.work-tile:nth-child(2){background:linear-gradient(#aa9c86,#6c6457)}
.work-tile:nth-child(3){background:linear-gradient(#6d7b86,#3f4a52)}
.work-tile:nth-child(4){background:linear-gradient(#9a7f68,#5a4b3f)}

/* mission + news */
.columns{height:1000px;padding-top:40px}
.columns .wrap{display:flex;gap:40px}
.mission{width:720px}
.news{width:320px}
.col-title{font-size:30px;text-transform:uppercase;margin-bottom:20px;border-bottom:2px solid var(--line);padding-bottom:6px}
.news .col-title{text-transform:none}
.mission-item{display:flex;gap:24px;margin-bottom:48px}
.video{width:300px;height:200px;flex:none;background:linear-gradient(#3a3a3a,#151515);position:relative}
.video .bar{position:absolute;left:0;right:0;bottom:0;height:22px;background:rgba(0,0,0,.7)}
.mission-item h3{font-size:16px;text-transform:uppercase;margin-bottom:8px;line-height:1.3}
.mission-item p{color:var(--muted);margin-bottom:14px}
.news-item{margin-bottom:30px}
.news-img{height:150px;margin-bottom:10px}
.news-item:nth-child(2) .news-img{background:linear-gradient(#8b7b66,#5d5346)}
.news-item:nth-child(3) .news-img{background:var(--white);border:1px solid var(--line);display:flex;align-items:center;justify-content:center}
.news-item:nth-child(4) .news-img{background:linear-gradient(#7d8e70,#4f5c46)}
.news-img .store{font-family:"Open Sans",sans-serif;font-weight:700;font-size:28px;color:var(--ink)}
.news-item h4{font-size:15px;text-transform:uppercase;margin-bottom:4px}
.news-item p{color:var(--muted);font-size:12px;margin-bottom:10px}

/* donate */
.donate{height:330px;position:relative;background:linear-gradient(90deg,#6e6b66,#8d8a84 50%,#5f5c57)}
.donate-shade{position:absolute;inset:0;background:rgba(0,0,0,.35)}
.donate-copy{position:relative;text-align:center;color:var(--white);padding-top:40px}
.donate-copy h2{font-family:"Open Sans",sans-serif;font-style:italic;font-size:30px;line-height:1.35;margin:16px 0 24px}
.donate-copy h2 em{color:var(--orange)}
.donate-copy .btn{font-size:15px;padding:10px 30px}

/* footer */
.footer-space{height:130px}
.footer{height:32px;background:var(--footer);color:#999;font-size:11px;text-align:center;line-height:32px}
</style>
</head>
<body>
<div class="topbar"><div class="wrap">
  <div><span>(555) 014-2290</span><span>hello@brightwellgiving.org</span></div>
  <div>Follow us on social</div>
</div></div>

<header class="header"><div class="wrap">
  <div class="brand"><span class="brand-mark"></span><span class="brand-name">BRIGHTWELL GIVING</span></div>
  <nav class="nav">
    <a class="active" href="#">Home</a><a href="#">Missions</a><a href="#">Get Involved</a><a href="#">News</a><a href="#">About Us</a><a href="#">Sponsors</a><a href="#">Donate</a><a href="#">Wall of Fame</a>
  </nav>
  <div class="social"><i></i><i></i><i></i></div>
</div></header>

<section class="hero">
  <div class="hero-photo" role="img" aria-label="Photo of a smiling child in a warm outdoor setting"></div>
  <div class="hero-copy">
    <h1><em>Give a</em> helping hand to those who need it!</h1>
    <p>Superheroes do not necessarily wear capes, some are just like you with a giving heart.</p>
    <a class="btn" href="#">READ MORE</a>
  </div>
</section>

<section class="about"><div class="wrap">
  <div class="about-text">
    <h2>Brightwell Giving</h2>
    <p>Brightwell Giving Inc is a non-profit organization that was created for one purpose: helping families and individuals in our community. We collect gently used clothes and textiles and pass them to those who need them the most.</p>
    <p>Our volunteers work every week to sort, clean and deliver donations to shelters, schools and families in need across the region.</p>
    <p>Our mission is to give back to the community and to make a difference, one donation at a time, with the support of members and friends.</p>
  </div>
  <ul class="ticks">
    <li><svg width="14" height="14" viewBox="0 0 14 14"><path d="M2 7l3 3 7-7" fill="none" stroke="#3b8f2a" stroke-width="2"/></svg>We are an operator organization</li>
    <li><svg width="14" height="14" viewBox="0 0 14 14"><path d="M2 7l3 3 7-7" fill="none" stroke="#3b8f2a" stroke-width="2"/></svg>We are an operator organization</li>
    <li><svg width="14" height="14" viewBox="0 0 14 14"><path d="M2 7l3 3 7-7" fill="none" stroke="#3b8f2a" stroke-width="2"/></svg>We are an operator organization</li>
    <li><svg width="14" height="14" viewBox="0 0 14 14"><path d="M2 7l3 3 7-7" fill="none" stroke="#3b8f2a" stroke-width="2"/></svg>We are an operator organization</li>
    <li><svg width="14" height="14" viewBox="0 0 14 14"><path d="M2 7l3 3 7-7" fill="none" stroke="#3b8f2a" stroke-width="2"/></svg>We are an operator organization</li>
    <li><svg width="14" height="14" viewBox="0 0 14 14"><path d="M2 7l3 3 7-7" fill="none" stroke="#3b8f2a" stroke-width="2"/></svg>We are an operator organization</li>
  </ul>
</div></section>

<section class="work"><div class="wrap">
  <h2 class="section-title">Latest Our Work</h2>
  <div class="work-grid">
    <div class="work-tile" role="img" aria-label="Photo of volunteers sorting donated clothes"><span>Ukraine statements</span></div>
    <div class="work-tile" role="img" aria-label="Photo of a donation drive event"><span>Ukraine statements</span></div>
    <div class="work-tile" role="img" aria-label="Photo of volunteers delivering boxes"><span>Ukraine statements</span></div>
    <div class="work-tile" role="img" aria-label="Photo of a community gathering"><span>Ukraine statements</span></div>
  </div>
</div></section>

<section class="columns"><div class="wrap">
  <div class="mission">
    <h2 class="col-title">Some Our Mission</h2>
    <article class="mission-item">
      <div class="video" role="img" aria-label="Video still of a mission interview"><div class="bar"></div></div>
      <div><h3>Love thy neighbor - Elena</h3>
      <p>Hello Brightwell Giving team, I am a mother of two girls, one of whom has a difficult genetic disorder. Just a few years ago the day of our daughter's surgery changed everything. Your help with clothes for the whole family has made a real difference to us.</p>
      <a class="btn" href="#">Details</a></div>
    </article>
    <article class="mission-item">
      <div class="video" role="img" aria-label="Video still of an agriculture school project"><div class="bar"></div></div>
      <div><h3>Start planning to open agriculture school in Haiti 02-02-2017</h3>
      <p>A professional educational center is a new nonprofit organization whose young and students can learn from experts in studying vegetables and grains to protect the environment and grow food together with local families.</p>
      <a class="btn" href="#">Details</a></div>
    </article>
    <article class="mission-item">
      <div class="video" role="img" aria-label="Video still of a school budget meeting"><div class="bar"></div></div>
      <div><h3>Start planning the budget for agriculture school in Haiti 17-02-2017</h3>
      <p>Our staff and local officers, originally from the region, are now studying agriculture. The school will open to future students, and the budget covers teachers, land, tools and the first planting season.</p>
      <a class="btn" href="#">Details</a></div>
    </article>
  </div>
  <aside class="news">
    <h2 class="col-title">Latest News</h2>
    <div class="news-item">
      <div class="news-img" role="img" aria-label="Photo of donated food items"></div>
      <h4>Collect Fund</h4>
      <p>We are starting the charity project to collect funds on Saturday.</p>
    </div>
    <div class="news-item">
      <div class="news-img"><span class="store">Online Store</span></div>
      <h4>Brightwell Giving Online Store</h4>
      <p>April 4, 2017: Brightwell Giving started its own online store to sell clothing.</p>
    </div>
    <div class="news-item">
      <div class="news-img" role="img" aria-label="Photo of a street sale with clothes racks"></div>
      <h4>Brightwell Giving Street Sales</h4>
      <p>April 1, 2017: We opened our first outdoor marketing to sell clothing on the streets of the city.</p>
      <a class="btn" href="#">Details</a>
    </div>
  </aside>
</div></section>

<section class="donate">
  <div class="donate-shade" role="img" aria-label="Background photo of a group of people joining hands"></div>
  <div class="donate-copy">
    <svg width="70" height="60" viewBox="0 0 70 60" aria-hidden="true"><path d="M35 8 C28 0 16 6 22 16 L35 28 L48 16 C54 6 42 0 35 8Z" fill="none" stroke="#fff" stroke-width="2"/><path d="M6 40 Q20 30 32 44 L44 44 M64 40 Q50 30 38 44" fill="none" stroke="#fff" stroke-width="2"/><path d="M4 52 L66 52" stroke="#fff" stroke-width="2"/></svg>
    <h2>Any Help or <em>Donation</em> no matter how small,<br>Will be deeply appreciated and is much needed</h2>
    <a class="btn" href="#">Donate Now</a>
  </div>
</section>

<div class="footer-space"></div>
<footer class="footer">© 2017 Brightwell Giving Inc. All rights reserved.</footer>
</body>
</html>
```